2024 Presentation for Job Interviews- I have been laid off

Refresh the branding and design to help create a dynamic presentation using some of Veltrano branding look and feel. This is a presentation I will use for interview processes with prospective employers. I would like it to be something that differentiates me from my competition
https://www.veltrano-example.com/c/en/us/about.html

Target Market(s)

Employers

Colors
0094D4
00A9DD
6FCCEA
C7EBF8
E9F6FB

```html
<!DOCTYPE html>
<html lang="en">
<head>
<meta charset="utf-8">
<title>Americas Leader – Point of View Document</title>
<link href="https://fonts.googleapis.com/css2?family=Cinzel:wght@500;700&family=Fira+Sans:wght@400;500;600;700&display=swap" rel="stylesheet">
<style>
  :root{
    --blue-deep:#0094D4;
    --blue:#00A9DD;
    --blue-soft:#6FCCEA;
    --blue-pale:#C7EBF8;
    --blue-mist:#E9F6FB;
    --ink:#1d2630;
    --grey:#6b7580;
    --page:#eef2f5;
    --white:#ffffff;
    --black:#0b0c0e;
  }
  *{box-sizing:border-box;margin:0;padding:0}
  html,body{width:1200px;height:4108px;overflow:hidden}
  body{background:var(--page);font-family:"Fira Sans",Arial,sans-serif;color:var(--ink);position:relative}
  .slide{position:absolute;left:16px;width:1168px;background:var(--white);box-shadow:0 4px 16px rgba(20,40,60,.08)}
  .abs{position:absolute}
  .photo{position:absolute;border-radius:14px}

  /* cover */
  .cover{top:0;left:0;width:1200px;height:620px;background:var(--black);overflow:hidden;box-shadow:none}
  .cover-wedge{position:absolute;left:0;top:0}
  .portrait{left:150px;top:90px;width:400px;height:400px;border-radius:50%;border:10px solid var(--white);
    background:radial-gradient(circle at 50% 40%,#8a7868 0%,#4e5662 55%,#1f2a36 100%)}
  .cover-title{left:660px;top:130px;font-family:"Cinzel",Georgia,serif;font-weight:500;font-size:62px;line-height:1.12;color:var(--white);letter-spacing:2px}
  .cover-sub{left:664px;top:312px;color:var(--white);font-size:24px;font-weight:500;letter-spacing:1px}
  .cover-doc{left:664px;top:356px;color:var(--white);font-size:15px;font-weight:600;letter-spacing:1.5px}
  .cover-name{left:664px;top:388px;color:var(--blue);font-size:24px;font-weight:700;letter-spacing:1px}

  /* agenda */
  .agenda{top:720px;height:620px;border-radius:4px}
  .agenda-photo{left:104px;top:60px;width:480px;height:500px;border-radius:36px;
    background:linear-gradient(180deg,#f4f6f7 0%,#d9dde0 45%,#7c8186 100%)}
  .section-title{font-size:44px;font-weight:700;color:var(--blue)}
  .agenda .section-title{left:648px;top:92px}
  .agenda-list{left:648px;top:176px;list-style:none}
  .agenda-list li{font-size:22px;color:var(--grey);height:46px;display:flex;align-items:center}
  .agenda-list li::before{content:"";width:12px;height:12px;border-radius:50%;background:var(--blue-soft);margin-right:22px}

  /* what matters */
  .matters{top:1400px;height:640px;text-align:center}
  .matters-title{left:0;width:100%;top:40px;font-size:42px;font-weight:700;color:var(--blue)}
  .matters-title span{color:var(--ink)}
  .matters-sub{left:0;width:100%;top:104px;font-size:20px;line-height:1.5;color:var(--grey)}
  .ph-a{left:34px;top:180px;width:316px;height:190px;background:linear-gradient(135deg,#5b6470,#a3a9ae)}
  .ph-b{left:34px;top:384px;width:316px;height:220px;background:linear-gradient(135deg,#6d727a,#b9bcc0)}
  .ph-c{left:366px;top:180px;width:400px;height:424px;background:linear-gradient(180deg,#9ab27a,#5d6e4b 60%,#3f4a39)}
  .ph-d{left:782px;top:180px;width:352px;height:130px;background:linear-gradient(135deg,#4a4f57,#8b8f94)}
  .ph-e{left:782px;top:322px;width:352px;height:282px;background:linear-gradient(135deg,#2d3138,#6a6f77)}

  /* people impact */
  .impact{top:2080px;height:620px}
  .impact-photo{left:104px;top:60px;width:440px;height:500px;border-radius:24px;
    background:radial-gradient(circle at 50% 45%,#f0c64a 0%,#3a3a3a 45%,#0b0b0b 75%)}
  .impact .section-title{left:600px;top:60px}
  .impact-copy{left:600px;top:130px;width:520px;font-size:13.5px;line-height:1.7;color:var(--grey)}
  .impact-copy p+p{margin-top:18px}

  /* priorities */
  .priorities{top:2760px;height:620px;background:var(--blue-mist)}
  .priorities .section-title{left:0;width:100%;top:40px;text-align:center}
  .card{position:absolute;top:130px;width:340px;height:440px;background:var(--white);border-radius:22px;text-align:center;
    box-shadow:0 6px 18px rgba(0,80,130,.08);padding-top:40px}
  .card-icon{width:70px;height:70px;border-radius:50%;background:var(--blue);margin:0 auto 26px;display:flex;align-items:center;justify-content:center}
  .card-head{font-size:26px;font-weight:700;color:var(--ink)}
  .card-tag{font-size:17px;font-weight:700;color:var(--blue);margin:10px 0 18px}
  .card-line{font-size:18px;color:var(--grey);line-height:1.7}

  /* fy20 */
  .theme{top:3420px;height:660px}
  .badge{left:64px;top:140px;width:390px;height:390px;border-radius:50%;
    background:radial-gradient(circle,var(--white) 0 56%,var(--blue-pale) 56% 58%,var(--white) 58% 78%,var(--blue-deep) 78% 100%)}
  .theme .section-title{left:580px;top:90px}
  .theme-quote{left:580px;top:160px;width:540px;font-size:19px;font-weight:600;line-height:1.4;color:var(--ink)}
  .theme-list{left:580px;top:240px;width:540px;list-style:none}
  .theme-list li{font-size:15px;color:var(--grey);min-height:42px;display:flex;align-items:center}
  .theme-list li::before{content:"";flex:none;width:12px;height:12px;border-radius:50%;background:var(--blue-soft);margin-right:20px}
</style>
</head>
<body>

<section class="slide cover">
  <svg class="cover-wedge" width="1200" height="620" viewBox="0 0 1200 620" aria-hidden="true">
    <path d="M0 0 H620 C560 120 600 300 700 520 L720 620 H0 Z" fill="var(--blue-deep)"/>
    <path d="M0 540 H1200 V620 H0 Z" fill="var(--blue)"/>
  </svg>
  <div class="abs portrait" role="img" aria-label="Portrait photograph of the presenter"></div>
  <h1 class="abs cover-title">AMERICAS<br>LEADER</h1>
  <p class="abs cover-sub">CISG | MIG SPECIALISTS</p>
  <p class="abs cover-doc">POINT OF VIEW DOCUMENT</p>
  <p class="abs cover-name">DANIEL MARSH</p>
</section>

<section class="slide agenda">
  <div class="photo agenda-photo" role="img" aria-label="Photo of a businessman climbing a staircase toward bright sky"></div>
  <h2 class="abs section-title">AGENDA</h2>
  <ul class="abs agenda-list">
    <li>About Me</li>
    <li>Leadership Philosophy</li>
    <li>Qualifications</li>
    <li>Growth Strategy</li>
    <li>30-60-90 Day Plan</li>
    <li>Sponsors</li>
  </ul>
</section>

<section class="slide matters">
  <h2 class="abs matters-title"><span>MY</span> “WHAT MATTERS?”</h2>
  <p class="abs matters-sub">Servant Leadership | “Why We CAN” Mindset | Culture by Design |<br>Golden Rule | Be Present</p>
  <div class="photo ph-a" role="img" aria-label="Team group photo at an award event"></div>
  <div class="photo ph-b" role="img" aria-label="Team members holding certificates"></div>
  <div class="photo ph-c" role="img" aria-label="Outdoor team photo beside a statue"></div>
  <div class="photo ph-d" role="img" aria-label="Team on stage at an event"></div>
  <div class="photo ph-e" role="img" aria-label="Presenter speaking at a conference"></div>
</section>

<section class="slide impact">
  <div class="photo impact-photo" role="img" aria-label="Light bulb word cloud with the word impact"></div>
  <h2 class="abs section-title">PEOPLE IMPACT</h2>
  <div class="abs impact-copy">
    <p>I was able to get connected to our team through the leadership program back in 2012. From the beginning, I sensed that we cared deeply about growth, trust and learning. My early managers gave me room to try, fail and improve. I worked as an account manager, then led a regional team, and found my voice helping others succeed.</p>
    <p>Being chosen to join the mentor program pushed me to invest in people around me. Seeing peers grow into leaders became my favorite result, and it shaped how I coach, listen and build teams today.</p>
  </div>
</section>

<section class="slide priorities">
  <h2 class="abs section-title">PRIORITIES DEEPER DIVE</h2>
  <div class="card" style="left:64px">
    <div class="card-icon"><svg width="36" height="36" viewBox="0 0 24 24" fill="none" stroke="#fff" stroke-width="2"><path d="M9 18h6M10 21h4M12 3a6 6 0 0 0-4 10.5c.8.8 1 1.5 1 2.5h6c0-1 .2-1.7 1-2.5A6 6 0 0 0 12 3z"/></svg></div>
    <p class="card-head">INNOVATION</p>
    <p class="card-tag">UNLOCK SPECIALIST IMPACT</p>
    <p class="card-line">Subscription acceleration<br>Innovate and incubate to Scale<br>Global offensive</p>
  </div>
  <div class="card" style="left:414px">
    <div class="card-icon"><svg width="36" height="36" viewBox="0 0 24 24" fill="none" stroke="#fff" stroke-width="2"><circle cx="12" cy="12" r="3"/><path d="M12 2v3M12 19v3M2 12h3M19 12h3M5 5l2 2M17 17l2 2M5 19l2-2M17 7l2-2"/></svg></div>
    <p class="card-head">PROCESS</p>
    <p class="card-tag">DELIVER CUSTOMER OUTCOMES</p>
    <p class="card-line">Platform Selling<br>X – architecture solutions<br>Building strategy on Building BOMS</p>
  </div>
  <div class="card" style="left:764px">
    <div class="card-icon"><svg width="36" height="36" viewBox="0 0 24 24" fill="none" stroke="#fff" stroke-width="2"><path d="M3 20h18M6 16v4M11 12v8M16 8v12M4 11l6-5 4 3 6-6"/></svg></div>
    <p class="card-head">GROWTH</p>
    <p class="card-tag">BUILD THE GROWTH ENGINE</p>
    <p class="card-line">High performance culture<br>Best in class specialist experience<br>New engagement models</p>
  </div>
</section>

<section class="slide theme">
  <div class="abs badge" role="img" aria-label="Round team theme badge"></div>
  <h2 class="abs section-title">FY20 THEME:</h2>
  <p class="abs theme-quote">Kairos- “A time when conditions are right for the accomplishment of a crucial action the opportune and decisive moment”</p>
  <ul class="abs theme-list">
    <li>FY20 will begin with a Wave of significant Change</li>
    <li>Why this as a theme? “From a Non-Surfer”</li>
    <li>Tide matters, wind matters, wave conditions matter (external factors)</li>
    <li>Takes a lot of work and energy to paddle out (you have to want it)</li>
    <li>Lots of dangers (competition) reef, rip tides, sharks, other surfers</li>
    <li>Right wave, right length, go with the wave, lean into it, enjoy the ride</li>
    <li>Make the paddle out worth it!</li>
  </ul>
</section>

</body>
</html>
```